Beveradge Can Body Print Design - Serious Style

We need a package design for new company Australia.Our products are Canned Drinking Water. We manufacture revolutionary healthy hydrogen water. It is beneficial to human health. The water is filled in standard 250ml Aluminum Beverage cans, Can is 125mm high, diameter is 53mm. if we unfold the can into flat surface, its printable area is 164mm long x 125mm high. All the design will be fitted into this area with bleeding. We also need a logo (to be designed separately) and Wording "Hydroge Water" on the print. We hope to use an abstract design (ideally with 1 or a few simple lines) to reflex a drop or drops of water or current / waves of water in a simple pattern in mono or at most 2 colors. Example of the preferred logo can be found in the attachments. together with some real samples of similar water cans. The successful designers will be invited to the carton box package and other series of our product packages designs. (In the attachment, with a2.jpg, please refer the can design only. the other packages design will be launched in separate projects)
Target Market(s)
all people who drink canned water. in particular, those who pay more attention to healthy lifestyle
Industry/Entity Type
Health Product
Logo Text
something suggesting natural or healthy lifestyle. Or any shape resembles the Letter "H"
Requirements
Must have
- something related to drops or ponds of water, or water wave, or anything reminds water
Nice to have
- This product has substantial benefits to human health. and the methods to make this type of water are purely mechanical, natural, no any harmful chemicals involved. It is also environmental friendly. It is new, not many people recognize it for now. but it will surely go into peoples' daily lives for its substantial natural way of maintaining peoples' healthy-being

```html
<!DOCTYPE html>
<html lang="en">
<head>
<meta charset="utf-8">
<title>Velora Hydrogen Water – Can Label</title>
<link rel="stylesheet" href="https://fonts.googleapis.com/css2?family=Montserrat:wght@700&family=Quattrocento+Sans:wght@400&display=swap">
<style>
  :root {
    --stage-bg: #eeeeee;
    --stage-glow: #ffffff;
    --brand-navy: #232d4f;
    --brand-sky: #4aa3d6;
    --label-white: #ffffff;
    --label-blue-light: #3f8fd6;
    --label-blue: #1c66be;
    --label-blue-deep: #0f4ea6;
  }
  * { margin: 0; padding: 0; box-sizing: border-box; }
  html, body {
    width: 1200px;
    height: 1032px;
    overflow: hidden;
  }
  body {
    background: radial-gradient(ellipse at 55% 45%, var(--stage-glow) 0%, var(--stage-bg) 75%, #dcdcdc 100%);
    position: relative;
    font-family: "Quattrocento Sans", sans-serif;
  }
  .can-label {
    position: absolute;
    left: 420px;
    top: 158px;
    width: 370px;
    height: 702px;
    overflow: hidden;
  }
  .label-art {
    position: absolute;
    inset: 0;
    width: 100%;
    height: 100%;
  }
  .brand-dot {
    position: absolute;
    left: 167px;
    top: 100px;
    width: 34px;
    height: 34px;
    border-radius: 50%;
    background: var(--brand-sky);
  }
  .brand-name {
    position: absolute;
    left: 0;
    width: 100%;
    top: 170px;
    text-align: center;
    font-family: "Montserrat", sans-serif;
    font-weight: 700;
    font-size: 52px;
    line-height: 52px;
    letter-spacing: 1px;
    color: var(--brand-navy);
  }
  .brand-descriptor {
    position: absolute;
    left: 0;
    width: 100%;
    top: 220px;
    text-align: center;
    font-size: 19px;
    line-height: 19px;
    letter-spacing: 3px;
    color: var(--brand-sky);
  }
  .product-claim {
    position: absolute;
    left: 0;
    width: 100%;
    top: 486px;
    text-align: center;
    font-size: 34px;
    line-height: 44px;
    color: var(--label-white);
  }
  .product-note {
    position: absolute;
    left: 0;
    width: 100%;
    top: 594px;
    text-align: center;
    font-size: 12.5px;
    line-height: 16px;
    color: var(--label-white);
  }
  .product-volume {
    position: absolute;
    left: 0;
    width: 100%;
    top: 656px;
    text-align: center;
    font-size: 15px;
    line-height: 18px;
    color: var(--label-white);
  }
</style>
</head>
<body>
  <main class="can-label">
    <svg class="label-art" viewBox="0 0 370 702" role="img" aria-label="Blue water condensation droplet pattern fading into a white glow at the top">
      <defs>
        <linearGradient id="labelBlue" x1="0" y1="0" x2="0" y2="1">
          <stop offset="0" stop-color="#dde9f5"/>
          <stop offset="0.3" stop-color="#3f8fd6"/>
          <stop offset="0.6" stop-color="#1c66be"/>
          <stop offset="1" stop-color="#0f4ea6"/>
        </linearGradient>
        <radialGradient id="logoGlow" cx="0.5" cy="0.5" r="0.5">
          <stop offset="0" stop-color="#ffffff"/>
          <stop offset="0.65" stop-color="#ffffff"/>
          <stop offset="1" stop-color="#ffffff" stop-opacity="0"/>
        </radialGradient>
      </defs>
      <rect width="370" height="702" fill="url(#labelBlue)"/>
      <ellipse cx="185" cy="180" rx="215" ry="160" fill="url(#logoGlow)"/>
    </svg>
    <span class="brand-dot" aria-hidden="true"></span>
    <h1 class="brand-name">VELORA</h1>
    <p class="brand-descriptor">HYDROGEN WATER</p>
    <p class="product-claim">hydrogen enriched<br>drinking water</p>
    <p class="product-note">no any harmful chemicals involved</p>
    <p class="product-volume">250ml</p>
  </main>
</body>
</html>
```